Business Card Design Project

We are rebranding an existing automotive collision repair business. The business is called dentworks garage. I have attached logo but I'm not tied to that. I want to leave this wide open.

I want this card to say we are professional, competent, cutting edge. We are focused on customers and use a lot of the latest technology to make the customer experience different. We sign customers in on iPads. Paperwork I signed electronically and updates are sent via text, email, logging on a website or as they wish. I want this innovation and image to come through in our cards

Target Market(s)

60%. Women 40% men. Age 35-60

Industry/Entity Type

Automotive

Requirements
Must have
• The card must have name, title, phone,email, cell, web page

```html
<!DOCTYPE html>
<html lang="en">
<head>
<meta charset="utf-8">
<title>Dentworks Garage — Business Card</title>
<link rel="stylesheet" href="https://fonts.googleapis.com/css2?family=Roboto+Condensed:wght@300;400&display=swap">
<style>
  :root {
    --page-bg: #e9e9ea;
    --card-bg: #3a3a3b;
    --card-band-top: #3c3c3d;
    --card-band-bottom: #5a5a5c;
    --brand-green: #8dc63f;
    --text-light: #f2f2f2;
    --text-muted: #c9c9c9;
    --divider: #707070;
  }
  * { box-sizing: border-box; margin: 0; padding: 0; }
  html, body {
    width: 1200px;
    height: 900px;
    overflow: hidden;
    background: var(--page-bg);
  }
  .canvas {
    position: relative;
    width: 1200px;
    height: 900px;
  }
  .card {
    position: absolute;
    left: 278px;
    width: 640px;
    height: 360px;
    background: var(--card-bg);
    overflow: hidden;
  }
  .card--front { top: 56px; }
  .card--back { top: 467px; }

  /* Front */
  .brand {
    position: absolute;
    left: 0;
    right: 0;
    top: 240px;
    display: flex;
    justify-content: center;
    align-items: center;
    gap: 14px;
  }
  .brand__square {
    width: 16px;
    height: 16px;
    background: var(--brand-green);
  }
  .brand__name {
    font-family: "Roboto Condensed", "Arial Narrow", sans-serif;
    font-weight: 400;
    font-size: 50px;
    line-height: 1;
    color: var(--text-light);
  }
  .tagline {
    position: absolute;
    left: 0;
    right: 0;
    top: 306px;
    text-align: center;
    font-family: "Roboto Condensed", "Arial Narrow", sans-serif;
    font-weight: 300;
    font-size: 14px;
    letter-spacing: 0.3em;
    color: var(--text-muted);
    text-transform: uppercase;
  }

  /* Back */
  .back-band {
    position: absolute;
    left: 0;
    top: 0;
    width: 100%;
    height: 148px;
    background: linear-gradient(180deg, var(--card-band-top), var(--card-band-bottom));
    border-bottom: 6px solid var(--brand-green);
  }
  .contact {
    position: absolute;
    left: 0;
    right: 0;
    top: 208px;
    text-align: center;
    font-family: "Roboto Condensed", "Arial Narrow", sans-serif;
    font-weight: 300;
    color: var(--text-muted);
  }
  .contact__person {
    font-size: 19px;
    line-height: 1;
    margin-bottom: 30px;
  }
  .contact__title { font-size: 13px; }
  .contact__line {
    font-size: 19px;
    line-height: 26px;
  }
  .sep {
    display: inline-block;
    color: var(--divider);
    margin: 0 12px;
    font-size: 13px;
    vertical-align: 2px;
  }
</style>
</head>
<body>
  <main class="canvas">
    <section class="card card--front" aria-label="Card front">
      <div class="brand">
        <span class="brand__square"></span>
        <h1 class="brand__name">dentworks garage</h1>
      </div>
      <p class="tagline">Careful repairs, clear updates</p>
    </section>

    <section class="card card--back" aria-label="Card back">
      <div class="back-band"></div>
      <div class="contact">
        <p class="contact__person">Daniel Reyes<span class="sep">|</span><span class="contact__title">Proprietor</span></p>
        <p class="contact__line">88 Panel Lane Brookvale 2100</p>
        <p class="contact__line">daniel@dentworksgarage.com<span class="sep">|</span>www.dentworksgarage.com</p>
        <p class="contact__line">m.&nbsp; 0412 555 018<span class="sep">|</span>t. 03 5550 1842<span class="sep">|</span>f. 03 5550 1843</p>
      </div>
    </section>
  </main>
</body>
</html>
```